Take out menu for The Lantern Nook Café

I'd like to have my menu re imagined.
Menu: (see LanternNookCafe Current menu file)
- Using the "new menu" and "cater menu" files which are updated over the LanternNookCafe Current menu
- Should be able to fit onto 11 x 17 parallel fold design
- Similar to current menu with headings and menu descriptions
- I do not have a font preference, whatever you think looks great and is easily readable
- More creative layout
- No pics of real foods
- Keeping the colors in "Salad, Grill, Sandwich, etc"
- The Cover page needs to be more of a cover, with all the same information, just more creative layout using the new logo attached.
- Do not need the "Harborline Roasters" and "Bellavita" logos that are on the current menu..
- With the background colors I'd like to stay with either bright type of green to signify "fresh", bright yellow, sky blue and/or white.
- The ** menu items should be featured
- "LanternNookCafe Current Menu" cover has all the pertinent information that I would also like on the new menu. Front cover should include: Logo, address, phone, fax, email, hours, "Catering Trays Always Avaialable" "Visit thelanternnookcafe.com to see our weekly specials!" "Dine In, Take Out or Delivery" Facebook, Twitter, Instagram logos.
The above mentioned for the front cover do not need to be in that particular order.
- Prefer the logo to be over a white background always
- Back cover should have somewhere, maps shot (LNMap), "Free Parking" "Free Wireless" "Delivery Minimum $10"
- With the maps shot on back, please insert the logo where it currently says "The Lantern Nook Cafe"
The Lantern Nook Cafe is a breakfast and lunch cafe serving mostly corporate clientele. As the owner, I am laid back and whimsical and I'd like that to reflect in the designs. Nothing fancy or serious, that's not my intention with the design.
thelanternnookcafe.com
Any questions please ask. Thank you in advance to all the talented designers for working on my project, it is greatly appreciated!

```html
<!DOCTYPE html>
<html lang="en">
<head>
<meta charset="utf-8">
<title>The Lantern Nook Café — Take Out Menu</title>
<link rel="stylesheet" href="https://fonts.googleapis.com/css2?family=Josefin+Sans:wght@700&family=Federo&display=swap">
<style>
:root{
  --stage:#3a3a3c;
  --sun:#ece44a;
  --lime:#cfe05a;
  --leaf:#a7d16c;
  --ink:#2d6a27;
  --ink-deep:#23571d;
  --divider:#f4f6de;
  --ribbon-red:#d24a3a;
  --ribbon-green:#2f9a44;
  --white:#ffffff;
}
*{box-sizing:border-box;margin:0;padding:0}
html,body{width:1200px;height:798px;overflow:hidden;background:var(--stage)}
.spread{position:absolute;left:35px;top:35px;width:1130px;height:730px;
  background:linear-gradient(180deg,var(--sun) 0%,var(--lime) 45%,var(--leaf) 100%);
  display:flex;gap:2px;background-color:var(--divider)}
.panel{position:relative;flex:1;height:100%;
  background:linear-gradient(180deg,var(--sun) 0%,var(--lime) 45%,var(--leaf) 100%);
  color:var(--ink);font-family:"Federo",sans-serif;padding:0 30px 0 40px}
.section-title{font-family:"Josefin Sans",sans-serif;font-weight:700;font-size:15px;color:var(--ink-deep);letter-spacing:.3px;line-height:1}
.intro{font-size:6.6px;line-height:1.25;margin-top:4px}
.price-line{font-size:10px;margin:6px 0 8px}
.item{margin-bottom:8px}
.item-name{font-size:11.5px;line-height:1.15}
.item-desc{font-size:6.4px;line-height:1.25;margin-top:1px}
.note{font-size:9px;margin-top:4px}
.list{font-size:8.5px;line-height:1.3}
.art{position:absolute;opacity:.55}
.p-garden .section-title{margin-top:143px}
.p-grill .section-title{margin-top:35px}
.p-grill .item{margin-bottom:9.5px}
.p-sandwich .section-title{margin-top:78px}
.p-sandwich .item{margin-bottom:9px}
.p-sandwich .sub-title{margin-top:14px}
.p-breakfast .section-title{margin-top:35px}
.p-breakfast .item{margin-bottom:7.5px}
.disclaimer{position:absolute;left:40px;top:626px;font-size:7px;display:flex;align-items:center;gap:5px}
.disclaimer .square{width:6px;height:6px;background:var(--ink-deep)}
.ribbon{position:absolute;left:72px;top:665px;width:182px;height:28px}
.ribbon-text{position:absolute;left:24px;top:4px;width:156px;color:var(--white);font-size:7.4px;line-height:1.3;text-align:right}
</style>
</head>
<body>
<main class="spread">

  <section class="panel p-garden">
    <svg class="art" role="img" aria-label="Illustration of a salad bowl with vegetables" style="left:60px;top:40px" width="125" height="118" viewBox="0 0 125 118">
      <rect x="0" y="0" width="125" height="118" rx="40" fill="#b7c94a"/>
    </svg>
    <h2 class="section-title">GARDEN</h2>
    <p class="intro">Choose either on a bed of greens with homemade croutons or in a wheat, white or spinach wrap, served cold</p>
    <p class="price-line">Salad: SM. 4.50 &nbsp;Lg. 6.75 &nbsp;Wrap: 6.25</p>
    <div class="item"><p class="item-name">**Apple Walnut</p><p class="item-desc">Romaine lettuce, diced chicken, tomatoes, craisins, diced apple, crumbled bleu cheese, walnuts and ranch dressing</p></div>
    <div class="item"><p class="item-name">Caesar</p><p class="item-desc">Romaine lettuce, diced chicken, sliced egg, parmesan cheese and creamy caesar dressing</p></div>
    <div class="item"><p class="item-name">Turkey</p><p class="item-desc">Romaine lettuce, home cooked all natural turkey, bacon, tomatoes, bleu cheese and French dressing</p></div>
    <div class="item"><p class="item-name">Cali Cobb</p><p class="item-desc">Romaine lettuce, diced chicken, avocado, tomatoes, bacon, egg, bleu cheese crumbles and avocado ranch dressing</p></div>
    <div class="item"><p class="item-name">Greek</p><p class="item-desc">Spinach, diced chicken, black olives, tomatoes, red onions, cucumber, feta cheese and balsamic vinaigrette dressing</p></div>
    <div class="item"><p class="item-name">Asian Sesame</p><p class="item-desc">Romaine lettuce, diced chicken, mandarin oranges, sliced almonds, carrots, sesame seeds and Asian sesame dressing</p></div>
    <div class="item"><p class="item-name">Chef's</p><p class="item-desc">Romaine lettuce, home cooked all natural turkey, tavern ham, Swiss cheese, egg, bacon, tomatoes, red onions, cucumbers and Thousand Island dressing</p></div>
    <div class="item"><p class="item-name">Tomato, Mozzarella &amp; Spinach</p><p class="item-desc">Spinach, tomatoes, cucumbers, sautéed onions, fresh mozzarella and olive oil vinaigrette dressing</p></div>
    <div class="item"><p class="item-name">Tuna Salad Salad</p><p class="item-desc">Romaine lettuce, homemade all white tuna salad, Swiss cheese, tomatoes, carrots, red onions and balsamic vinaigrette dressing</p></div>
    <div class="item"><p class="item-name">House Garden Salad</p><p class="item-name" style="font-size:10px">Lg. 5.25 &nbsp;Sm. 1.95 &nbsp;Wrap: 5.50</p><p class="item-desc">Romaine lettuce, tomatoes, cucumber, carrots, red onions, shredded cheese blend and choice of dressing</p></div>
    <p class="item-desc" style="margin-top:10px">Dressings: Asian Sesame, Avocado Ranch, Balsamic Vinaigrette, Bleu Cheese, Creamy Caesar, Creamy Italian, Fat Free Raspberry Vinaigrette, French, Honey Mustard, Olive Oil Vinaigrette, Ranch, Thousand Island</p>
  </section>

  <section class="panel p-grill">
    <svg class="art" role="img" aria-label="Illustration of a grilled sausage on a fork" style="left:150px;top:520px" width="110" height="175" viewBox="0 0 110 175">
      <rect x="0" y="0" width="110" height="175" rx="30" fill="#a9cf5a"/>
    </svg>
    <h2 class="section-title">GRILL</h2>
    <div class="item" style="margin-top:2px"><p class="item-name">**Commerce Pita 6.25</p><p class="item-desc">Grilled chicken, provolone, spinach, bacon and ranch on pita bread. Kick it up and ask for cajun seasoning!</p></div>
    <div class="item"><p class="item-name">Philly Cheesesteak 5.95</p><p class="item-desc">Beef or chicken with choice of cheese. Toppings .25 each</p></div>
    <div class="item"><p class="item-name">Burger/Veggie Burger 5.95</p><p class="item-desc">Beef or veggie on a kaiser roll with choice of cheese, lettuce, tomato and red onion</p></div>
    <div class="item"><p class="item-name">Barbecue Chicken Panini 6.25</p><p class="item-desc">Grilled chicken, BBQ sauce, red onions, bacon, cheddar cheese and ranch on sourdough</p></div>
    <div class="item"><p class="item-name">Fajita Wrap 6.25</p><p class="item-desc">Seasoned chicken, peppers, onions and mixed cheese in a wrap, served with sour cream and salsa</p></div>
    <div class="item"><p class="item-name">Reuben / Rachel 6.25</p><p class="item-desc">Choose from home cooked all natural turkey, home cooked roast beef or tavern ham, with kraut or coleslaw, Swiss and Thousand Island on marble rye</p></div>
    <div class="item"><p class="item-name">Veggie Panini 6.25</p><p class="item-desc">Fresh mozzarella cheese, spinach, tomato, cucumber, red onions, roasted red peppers and balsamic vinaigrette on whole grain bread</p></div>
    <div class="item"><p class="item-name">Cajun Chicken Sandwich 6.25</p><p class="item-desc">Grilled chicken with cajun seasoning, provolone or pepper jack cheese, onions, tomato and ranch on a kaiser roll</p></div>
    <div class="item"><p class="item-name">Chicken Mozz Panini 6.50</p><p class="item-desc">Grilled chicken, tomatoes, spinach balsamic vinaigrette and fresh mozzarella on sourdough</p></div>
    <div class="item"><p class="item-name">California Club Sandwich 6.50</p><p class="item-desc">Grilled chicken, fresh avocado, bacon, Swiss, lettuce, tomato and honey mustard on a kaiser roll</p></div>
    <div class="item"><p class="item-name">Chipotle Ranch Turkey Pita 6.50</p><p class="item-desc">Home cooked all natural turkey, bacon, red onion, pepper-jack cheese and chipotle ranch on pita bread</p></div>
    <div class="item"><p class="item-name">Hot Roast Beef 6.50</p><p class="item-desc">Home cooked roast beef in au jus, sautéed onions, horseradish sauce and provolone cheese baked on a hoagie roll</p></div>
    <div class="item"><p class="item-name">Tuna Melt 6.50</p><p class="item-desc">Homemade all white tuna salad, tomatoes, and Swiss baked on sourdough</p></div>
    <div class="item"><p class="item-name">Mediterranean Panini 6.50</p><p class="item-desc">Grilled chicken, fresh mozzarella, roasted peppers and spinach on sourdough</p></div>
    <div class="item"><p class="item-name">Crazy Cheese 4.25</p><p class="item-desc">Cheddar, American, Swiss, and tomato on sourdough. Add bacon 1.50</p></div>
    <p class="note" style="text-align:center;padding-right:40px">~ Add chips and a pickle .50 ~</p>
  </section>

  <section class="panel p-sandwich">
    <svg class="art" role="img" aria-label="Illustration of a sandwich wedge" style="left:95px;top:30px" width="165" height="75" viewBox="0 0 165 75">
      <polygon points="0,40 90,0 165,40 165,75 0,75" fill="#a8c94a"/>
    </svg>
    <h2 class="section-title">SANDWICHES</h2>
    <p class="intro" style="margin-top:2px;margin-bottom:6px">On choice of bread or wrap</p>
    <div class="item"><p class="item-name">** Turkey Club 6.50</p><p class="item-desc">A triple decker! Home cooked all natural turkey, tomato, bacon, lettuce, Swiss and mayo. Add sun-dried tomato pesto .25</p></div>
    <div class="item"><p class="item-name">B.L.T. 5.25</p><p class="item-desc">A true classic with bacon, iceberg lettuce, tomato and mayo</p></div>
    <div class="item"><p class="item-name">Junkyard 6.50</p><p class="item-desc">Home cooked roast beef, home cooked all natural turkey, tavern ham, pepperoni, lettuce, tomato, Swiss and mayo</p></div>
    <div class="item"><p class="item-name">Cold Roast Beef 6.50</p><p class="item-desc">Home cooked roast beef, lettuce, tomato, Swiss and spicy horseradish sauce</p></div>
    <div class="item"><p class="item-name">Tuna Salad 6.50</p><p class="item-desc">Homemade all white tuna, with lettuce and tomato. Add cheese .25</p></div>
    <div class="item"><p class="item-name">Veggie Avocado 6.50</p><p class="item-desc">Avocado, roasted peppers, cucumber, red onions, feta cheese, lettuce, tomato and balsamic vinaigrette</p></div>
    <div class="item"><p class="item-name">Turkey Bacon Ranch 6.50</p><p class="item-desc">Home cooked all natural turkey, bacon, cheddar cheese, lettuce, tomato and ranch</p></div>
    <div class="item"><p class="item-name">Italian 6.50</p><p class="item-desc">Cappicola, salami, pepperoni, provolone, lettuce, tomato and onion</p></div>
    <div class="item"><p class="item-name">Ham and Swiss 6.25</p><p class="item-desc">Sliced tavern ham and Swiss with lettuce, tomato, mayo and mustard</p></div>
    <div class="item"><p class="item-name">Chicken Salad 6.25</p><p class="item-desc">Made to order with lettuce and tomato. Add cheese .25</p></div>
    <div class="item"><p class="item-name">Egg Salad 5.95</p><p class="item-desc">Made to order with lettuce and tomato. Add cheese .25</p></div>
    <div class="item"><p class="item-name">PBB&amp;J 4.95</p><p class="item-desc">Peanut butter or Cocoanut Creme and jelly with bananas, lightly grilled</p></div>
    <p class="note">~ add chips and a pickle .50 ~</p>
    <h2 class="section-title sub-title">COMBOS</h2>
    <p class="list" style="margin-top:3px">Choose two. 6.50<br>½ Sandwich<br>½ Salad<br>Soup<br>Quiche</p>
    <h2 class="section-title sub-title">SOUP</h2>
    <p class="list" style="margin-top:3px">8oz – 3.15<br>12oz – 3.50<br>*Some soups .50 extra*</p>
  </section>

  <section class="panel p-breakfast">
    <svg class="art" role="img" aria-label="Illustration of a muffin with fruit on top" style="left:150px;top:485px" width="115" height="125" viewBox="0 0 115 125">
      <rect x="0" y="0" width="115" height="125" rx="35" fill="#a9cf5a"/>
    </svg>
    <h2 class="section-title">BREAKFAST</h2>
    <div class="item" style="margin-top:2px"><p class="item-name">**Cheesesteak Breakfast Wrap 4.50</p><p class="item-desc">Two eggs, chopped steak, onions and American cheese in a wrap</p></div>
    <div class="item"><p class="item-name">Breakfast Sandwich 3.50</p><p class="item-desc">Two eggs and American cheese on toast or English muffin with choice of meat<br>• On a bagel add .50<br>• On a croissant add 1.00</p></div>
    <div class="item"><p class="item-name">Eggs Your Way 3.75</p><p class="item-desc">Two eggs cooked to order with meat and toast</p></div>
    <div class="item"><p class="item-name">Omelet 4.50</p><p class="item-desc">2 eggs with your choice of up to 3 fillings and toast</p></div>
    <div class="item"><p class="item-name">Burrito 4.50</p><p class="item-desc">Two eggs, meat, mixed cheese, onions, peppers and salsa in a wrap</p></div>
    <div class="item"><p class="item-name">Greek Pita 4.50</p><p class="item-desc">Two eggs, spinach and feta on a pita</p></div>
    <div class="item"><p class="item-name">Avocado Egg Croissant 4.50</p><p class="item-desc">Two eggs, avocado and cheddar cheese on a croissant</p></div>
    <div class="item"><p class="item-name">B.E.L.T 4.50</p><p class="item-desc">Egg, bacon, lettuce and tomato on choice of toast or English muffin. Add cheese .25</p></div>
    <div class="item"><p class="item-name">French Toast 4.50</p><p class="item-desc">Two thick slices of brioche with choice of meat</p></div>
    <div class="item"><p class="item-name">Pancakes 4.25</p><p class="item-desc">Three pancakes with choice of meat</p></div>
    <div class="item"><p class="item-name">Quiche 3.75</p></div>
    <div class="item"><p class="item-name">Bagel 2.15</p><p class="item-desc">Toasted with cream cheese, butter or jelly</p></div>
    <div class="item"><p class="item-name">Croissant 1.95</p></div>
    <div class="item"><p class="item-name">Muffin 1.95</p></div>
    <div class="item"><p class="item-name">English Muffin 1.55</p></div>
    <div class="item"><p class="item-name">Side of hash browns 1.50</p></div>
    <div class="item"><p class="item-name">Side of meat 1.50</p><p class="item-desc">Bacon, sausage, ham, turkey sausage or pork roll</p></div>
    <div class="item"><p class="item-name">Toast 1.25</p></div>
    <p class="disclaimer"><span class="square"></span>Menu items and prices subject to change</p>
    <div class="ribbon">
      <svg width="182" height="28" viewBox="0 0 182 28" aria-hidden="true">
        <polygon points="0,4 24,4 24,24 0,24 8,14" fill="var(--ribbon-red)"/>
        <rect x="18" y="0" width="164" height="28" fill="var(--ribbon-green)"/>
      </svg>
      <p class="ribbon-text">If you don't see what you want on the menu, we will try and make it for you!</p>
    </div>
  </section>

</main>
</body>
</html>
```